Wordpress template re-design of current website

We need a WordPress template design and new look for our existing website. Our existing site it located at www.velmoro.com.au We are a tech company and want a fresh, clean modern website that matches our brand, services and logo colors. Our main Services are hospitality solutions, Velmoro TV solution and managed networks, more information on these can come from our existing website.

Target Market(s)

We are a tech company so must have a modern feel for new technology

Industry/Entity Type

It Company

Number of Pages Required

5+ page

Font styles to use
Sans Serif

Requirements
Must have
• Be based on a wordpress templete design and match the services that we have in our existing website, in the testimonials want a place for video testimonials as well as text. Nice clean icons used for graphics to represent services.
Nice to have
• nice visual representation of our services in the way of clean icons etc
Should not have
• Clutter

```html
<!DOCTYPE html>
<html lang="en">
<head>
<meta charset="utf-8">
<title>Velmoro – Our News</title>
<link href="https://fonts.googleapis.com/css2?family=Roboto:wght@400;500;700&family=Lato:wght@400;700&display=swap" rel="stylesheet">
<style>
:root{
  --brand:#0b3f8c;
  --navy:#073d86;
  --slate:#5e7283;
  --footer:#6b7e8e;
  --card-body:#ebebeb;
  --placeholder:#6e7f8e;
  --text:#6a6a6a;
  --white:#ffffff;
}
*{margin:0;padding:0;box-sizing:border-box}
html,body{width:797px;height:1200px;overflow:hidden;background:var(--white)}
body{position:relative;font-family:'Lato',sans-serif;color:var(--text)}
.abs{position:absolute}
.logo{left:49px;top:22px;font:700 30px/1 'Roboto',sans-serif;color:var(--brand);display:flex;align-items:center;gap:8px}
.logo .dot{width:14px;height:14px;border-radius:50%;background:var(--brand)}
.phone{left:556px;top:29px;display:flex;align-items:center;gap:6px;font:400 12.5px 'Roboto',sans-serif;color:#555}
.portal{left:666px;top:25px;width:82px;height:26px;border-radius:13px;background:var(--brand);color:#fff;font:700 11px/26px 'Roboto',sans-serif;text-align:center}
.nav{left:0;top:77px;width:797px;height:33px;background:var(--slate)}
.nav a{position:absolute;top:0;font:700 10.5px/33px 'Roboto',sans-serif;color:#fff;text-decoration:none}
.search{left:571px;top:83px;width:177px;height:20px;border-radius:10px;background:#fff;font:italic 9px/20px 'Lato',sans-serif;color:#999;padding-left:23px}
.search svg{position:absolute;left:8px;top:5px}
.hero{left:0;top:110px;width:797px;height:153px;background:linear-gradient(90deg,#8a96a1 0%,#a3adb6 35%,#8ea1b8 60%,#7c93b3 100%)}
.hero h1{position:absolute;left:49px;top:67px;font:700 20px 'Roboto',sans-serif;color:#fff}
.card{width:221px;height:330px}
.card .media{position:absolute;left:0;top:0;width:221px;height:147px}
.card .tab{position:absolute;left:0;top:12px;height:21px;width:134px;background:#fff;clip-path:polygon(0 0,100% 0,94% 50%,100% 100%,0 100%);font:500 12px/21px 'Roboto',sans-serif;color:#111;padding-left:12px;white-space:nowrap}
.card .title{position:absolute;left:0;top:147px;width:221px;height:58px;background:var(--navy);color:#fff;font:500 12px/12.5px 'Roboto',sans-serif;padding:17px 0 0 18px}
.card .title:after{content:"";position:absolute;left:20px;bottom:-7px;border-left:7px solid transparent;border-right:7px solid transparent;border-top:7px solid var(--navy)}
.card .body{position:absolute;left:0;top:205px;width:221px;height:125px;background:var(--card-body);font:400 9.2px/14.7px 'Lato',sans-serif;color:var(--text);padding:22px 20px 0 18px}
.footer{left:0;top:1003px;width:797px;height:169px;background:var(--footer);color:#fff;box-shadow:inset 0 3px 4px -1px rgba(0,0,0,.45)}
.footer h4{position:absolute;top:30px;font:500 10.5px 'Roboto',sans-serif}
.footer ul{position:absolute;top:55px;list-style:none;font:400 8.6px/16px 'Lato',sans-serif}
.footer .info{position:absolute;font:400 8.6px/11px 'Lato',sans-serif}
.field{position:absolute;left:468px;width:206px;height:24px;background:#fff;border-radius:3px;font:400 9px/24px 'Lato',sans-serif;color:#888;padding-left:20px}
.field i{position:absolute;left:7px;top:8px;width:8px;height:8px;border-radius:2px;background:#8a95a0}
.signup{left:680px;top:1093px;width:68px;height:54px;border-radius:4px;background:#8596a5;color:#fff;font:500 10.5px 'Roboto',sans-serif;text-align:center;padding-top:10px}
.copyright{left:49px;top:1181px;font:400 8.6px 'Lato',sans-serif;color:#777}
.chat{left:604px;top:1178px;width:144px;height:22px;border-radius:4px 4px 0 0;background:linear-gradient(#9aa3ab,#6e7780);color:#e8e8e8;font:400 8px/22px 'Lato',sans-serif;padding-left:26px}
</style>
</head>
<body>
<header>
  <div class="abs logo"><span>Velmoro</span><span class="dot"></span></div>
  <div class="abs phone">
    <svg width="18" height="18" viewBox="0 0 18 18"><circle cx="9" cy="9" r="9" fill="var(--brand)"/><path d="M6 5l2 2-1 1c.6 1.3 1.7 2.4 3 3l1-1 2 2-1.4 1.2C8.5 12.8 5.2 9.5 4.8 6.4z" fill="#fff"/></svg>
    <span>1300 555 019</span>
  </div>
  <div class="abs portal">PORTAL</div>
</header>
<nav class="abs nav">
  <a style="left:74px">HOME</a>
  <a style="left:153px">SERVICES</a>
  <a style="left:249px">ABOUT</a>
  <a style="left:332px">OUR WORK</a>
  <a style="left:434px">CONTACT</a>
</nav>
<div class="abs search"><svg width="10" height="10" viewBox="0 0 10 10"><circle cx="4" cy="4" r="3" fill="none" stroke="#555" stroke-width="1.3"/><path d="M6.3 6.3L9 9" stroke="#555" stroke-width="1.3"/></svg>Search</div>
<section class="abs hero" role="img" aria-label="Photo of businessmen reading a newspaper together"><h1>OUR NEWS</h1></section>

<main>
  <article class="abs card" style="left:49px;top:294px">
    <div class="media" role="img" aria-label="Photo of a hotel entrance at dusk" style="background:linear-gradient(180deg,#7a5a45,#a8683a 60%,#5c4330)"></div>
    <div class="tab">Harbourline</div>
    <h3 class="title">Harbourline Sydney<br>Completed August 2015</h3>
    <p class="body">Lorem ipsum dolor sit amet, consectetur adipisicing elit, sed do eiusmod tempor incididunt ut labore et dolore magna aliqua. Ut enim ad minim veniam, quis nostrud exercitation ullamco laboris nisi ut aliquip ex ea commodo consequat.</p>
  </article>
  <article class="abs card" style="left:288px;top:294px">
    <div class="media" role="img" aria-label="Photo of a laptop and a phone showing a wifi login page" style="background:linear-gradient(180deg,#2a2a2e,#55565a 60%,#bdbab4)"></div>
    <div class="tab">Kestrel Apartment</div>
    <h3 class="title">Kestrel Brisbane<br>Launch Wifi Zone</h3>
    <p class="body">Lorem ipsum dolor sit amet, consectetur adipisicing elit, sed do eiusmod tempor incididunt ut labore et dolore magna aliqua. Ut enim ad minim veniam, quis nostrud exercitation ullamco laboris nisi ut aliquip ex ea commodo consequat.</p>
  </article>
  <article class="abs card" style="left:527px;top:294px">
    <div class="media" role="img" aria-label="Photo of a white coach bus" style="background:linear-gradient(180deg,#6d8fc0,#e8ecef 45%,#d8d8d8 80%,#6b6b6b)"></div>
    <div class="tab">Coastrider</div>
    <h3 class="title">Wifi Onboard at<br>Coastrider Coach</h3>
    <p class="body">Lorem ipsum dolor sit amet, consectetur adipisicing elit, sed do eiusmod tempor incididunt ut labore et dolore magna aliqua. Ut enim ad minim veniam, quis nostrud exercitation ullamco laboris nisi ut aliquip ex ea commodo consequat.</p>
  </article>

  <article class="abs card" style="left:49px;top:642px">
    <div class="media" role="img" aria-label="Placeholder news illustration" style="background:var(--placeholder)"></div>
    <div class="tab">Lorem Ipsum</div>
    <h3 class="title">Contrary to popular belief,<br>Lorem Ipsum is random text</h3>
    <p class="body">Lorem ipsum dolor sit amet, consectetur adipisicing elit, sed do eiusmod tempor incididunt ut labore et dolore magna aliqua. Ut enim ad minim veniam, quis nostrud exercitation ullamco laboris nisi ut aliquip ex ea commodo consequat.</p>
  </article>
  <article class="abs card" style="left:288px;top:642px">
    <div class="media" role="img" aria-label="Placeholder news illustration" style="background:var(--placeholder)"></div>
    <div class="tab">Lorem Ipsum</div>
    <h3 class="title">Contrary to popular belief,<br>Lorem Ipsum is random text</h3>
    <p class="body">Lorem ipsum dolor sit amet, consectetur adipisicing elit, sed do eiusmod tempor incididunt ut labore et dolore magna aliqua. Ut enim ad minim veniam, quis nostrud exercitation ullamco laboris nisi ut aliquip ex ea commodo consequat.</p>
  </article>
  <article class="abs card" style="left:527px;top:642px">
    <div class="media" role="img" aria-label="Placeholder news illustration" style="background:var(--placeholder)"></div>
    <div class="tab">Lorem Ipsum</div>
    <h3 class="title">Contrary to popular belief,<br>Lorem Ipsum is random text</h3>
    <p class="body">Lorem ipsum dolor sit amet, consectetur adipisicing elit, sed do eiusmod tempor incididunt ut labore et dolore magna aliqua. Ut enim ad minim veniam, quis nostrud exercitation ullamco laboris nisi ut aliquip ex ea commodo consequat.</p>
  </article>
</main>

<footer class="abs footer">
  <h4 style="left:49px">QUICK LINKS</h4>
  <ul style="left:49px"><li>Home</li><li>Services</li><li>About</li><li>Our Work</li><li>Contact</li></ul>
  <h4 style="left:168px">USEFUL LINKS</h4>
  <ul style="left:168px"><li>Case Studies</li><li>Testimonials</li><li>News</li><li>Resellers</li></ul>
  <h4 style="left:310px">CONTACT US</h4>
  <svg class="abs" style="left:311px;top:56px" width="8" height="11" viewBox="0 0 8 11"><path d="M4 11C1 7 0 5.5 0 4a4 4 0 018 0c0 1.5-1 3-4 7z" fill="#8e9eab"/></svg>
  <div class="info" style="left:325px;top:55px">42 Harbour Lane<br>Ridgeview, QLD 4210</div>
  <svg class="abs" style="left:311px;top:102px" width="10" height="10" viewBox="0 0 10 10"><path d="M2 1l2 2-1 1c.5 1 1.3 1.8 2.3 2.3l1-1 2 2-1.2 1.2C4 8 1.5 5.5.8 2.2z" fill="#8e9eab"/></svg>
  <div class="info" style="left:325px;top:102px">1300 555 019</div>
  <svg class="abs" style="left:310px;top:121px" width="11" height="9" viewBox="0 0 11 9"><path d="M0 3L5.5 0 11 3v6H0z" fill="#8e9eab"/></svg>
  <div class="info" style="left:326px;top:120px">sales@velmoro.com.au</div>
  <h4 style="left:467px">NEWSLETER SIGN UP</h4>
  <div class="info" style="left:468px;top:54px;line-height:16px">Enter your name and email to subscribe or unsubscribe to<br>receive  latest news &amp; offers!!!</div>
</footer>
<div class="field" style="top:1093px"><i></i>Enter Your Name</div>
<div class="field" style="top:1124px"><i></i>Enter Your Email</div>
<div class="abs signup">
  <svg width="20" height="18" viewBox="0 0 20 18"><path d="M19 0L0 8l6 2 1 7 3-5 5 3z" fill="#fff"/></svg><br>SIGN UP
</div>
<div class="abs copyright">© Copyright 2015 Velmoro Wireless Internet All Rights Reserved.</div>
<div class="abs chat">Live Chat Offline</div>
</body>
</html>
```